Inspirational quotes poster shop seeks poster designs

Hi! We are launching an eshop with design posterss featuring inspirational quotes. We need a first poster design while looking for further cooperation on around 20 poster designs. We need outputs in the format that can go to high quality print (size at least 100x70cm).

For the first design feel free to choose any of the following quotes to depict:

1. "Stop starting. Start finishing." Author: Torvald Essunger, Klangora
2. "A problem well stated is a problem half solved." Author: Walter P. Brimsley, American inventor
3. "The best way to predict the future is to invent it." Author: Dale Hubbs, Quince

Designs should be rarther simple, think please of your whole concept and how various posters would go together. Every poster can be quite different though, in terms of fonts, colours and overall design, together they should however form and interesting collage.

Designs must contain the quote, author & company. it can be pure text or some indication of the sense of the quote.

Design must also feature company name/logo (not available yet, for now please use "thoughtvolta" as a working name), QR code with a title "Read the story"

See these posters for design we like (for inspiration ONLY!):
http://www.launchtonics.example/products/launch-print-its-simple-until-you-make-it-complicated
http://www.launchtonics.example/products/launch-print-marcus-feldane-less-meetings-more-doing
http://www.launchtonics.example/products/launch-print-gordon-ashfeld-stop-sketching-start-building

Hi to everybody! Sorry for the spam, some of you have been struggling with finding the crux in the quote, so here I offer some ideas what to look for in them. It's up to you to take it, leave it or change it:)

Stop starting, start finishing -
1 - stop starting with many times repeated small word starting, perhaps large word starting made of small words starting, with it contrasting start finishing in normal bold font.
2 - STARTING could look quite unfinished, sketchy, especially -ING could look more unfinished then the rest , e.g. just rough indication of outline of the letters, again contrasting with start finishing will clean & neat writting.

Problem well stated is a problem half solved - look for something that is clearer by defining the problem. Perhaps in a simple sketch like here http://www.launchtonics.example/products/launch-print-its-simple-until-you-make-it-complicated  point out a route from a problem (light = flame), to a solution (lightbulb, lightbulb design drawing or something like that).

Anyway, despite preference for simple design, I am still looking for some smart, creative, catchy idea in the design. Check with yourself if it's something you can would want to buy and hang up on your wall.

Good luck to all of you and again, thank you all very much for participation!
Radim

Target Market(s)

businesses of every size, from startups to large corporates seeking culture change or motivation kick up

Industry/Entity Type

Shop

Requirements
Must have
• I strongly prefer portrait orientation of the poster!

Nice to have
• Quotes themselves are often on the edge, teasing, so the design can be.
Should not have
• Try to avoid traditional dialoge bubble for the quote itself as the first obvious idea for depicting a quote.

Avoid using photos (not simple then) or too many colours.

Of course, by no means use a COPY of existing designs I linked to for inspiration. It just shows what we like.

```html
<!DOCTYPE html>
<html lang="en">
<head>
<meta charset="utf-8">
<title>Stop Starting. Start Finishing. – thoughtvolta poster</title>
<link href="https://fonts.googleapis.com/css2?family=Source+Sans+3:wght@300;400;700&display=swap" rel="stylesheet">
<style>
  :root {
    --backdrop: #d9d9d9;
    --poster: #3b3b3d;
    --yellow: #ffc90b;
    --white: #ffffff;
    --quote-grey: #7f7f80;
  }
  html, body {
    margin: 0;
    padding: 0;
    overflow: hidden;
  }
  body {
    width: 1200px;
    height: 1000px;
    background: var(--backdrop);
    position: relative;
    font-family: "Source Sans 3", "Myriad Pro", sans-serif;
  }
  .poster {
    position: absolute;
    left: 315px;
    top: 101px;
    width: 575px;
    height: 806px;
    background: var(--poster);
    overflow: hidden;
  }
  .brand-ribbon {
    position: absolute;
    left: 453px;
    top: 0;
    width: 50px;
    height: 162px;
  }
  .brand-ribbon svg { display: block; }
  .brand-name {
    position: absolute;
    left: 25px;
    top: 68px;
    transform: translate(-50%, -50%) rotate(-90deg);
    white-space: nowrap;
    font-size: 14px;
    font-weight: 700;
    color: var(--poster);
    letter-spacing: 0.2px;
  }
  .brand-dot {
    position: absolute;
    left: 20px;
    top: 111px;
    width: 10px;
    height: 10px;
    border-radius: 50%;
    background: var(--poster);
  }
  .quote-mark {
    position: absolute;
    color: var(--quote-grey);
    font-weight: 700;
    font-size: 136px;
    line-height: 1;
  }
  .quote-mark--open { left: 26px; top: 256px; }
  .quote-mark--close { left: 494px; top: 345px; }
  .quote {
    position: absolute;
    right: 82px;
    top: 277px;
    margin: 0;
    text-align: left;
  }
  .quote-line {
    display: block;
    font-size: 58px;
    line-height: 55px;
    color: var(--white);
    white-space: nowrap;
  }
  .quote-line--stop { font-weight: 300; letter-spacing: -1.5px; }
  .quote-line--start { font-weight: 700; letter-spacing: -2px; }
  .quote-highlight { color: var(--yellow); }
  .attribution {
    position: absolute;
    right: 80px;
    top: 394px;
    margin: 0;
    font-size: 20px;
    font-weight: 400;
    letter-spacing: 1.2px;
    color: var(--white);
    white-space: nowrap;
  }
  .torn-band {
    position: absolute;
    left: 0;
    top: 528px;
    width: 575px;
    height: 96px;
    background: var(--yellow);
  }
</style>
</head>
<body>
  <main class="poster">
    <div class="brand-ribbon">
      <svg width="50" height="162" viewBox="0 0 50 162" aria-hidden="true">
        <polygon points="0,0 50,0 50,162 0,139" fill="var(--white)"/>
      </svg>
      <span class="brand-name">thoughtvolta</span>
      <span class="brand-dot"></span>
    </div>

    <span class="quote-mark quote-mark--open" aria-hidden="true">&ldquo;</span>
    <blockquote class="quote">
      <span class="quote-line quote-line--stop">STOP STARTING.</span>
      <span class="quote-line quote-line--start">START <span class="quote-highlight">FINISHING</span></span>
    </blockquote>
    <span class="quote-mark quote-mark--close" aria-hidden="true">&rdquo;</span>
    <p class="attribution">Torvald Essunger, Klangora</p>

    <div class="torn-band" role="img" aria-label="Yellow paper band torn apart in the middle, the tear not yet finished"></div>
  </main>
</body>
</html>
```